Marlow Landscaping Landing Page

I require a landing page for my landscaping business.

My business plan revolves around hooking clients with weeding services. Not lawn herbicide sprays, but actual hand weeding and bed maintenance. I've found my niche as most people do not want to do this kind of work. From there I often upsell clients into actual hardscaping or softscaping.

I like things to be clean, concise, and to the point. Not overly flashy, but not so minimal that that it's boring. My logo is a very good example of what I like.

The business is LGBTQ owned and operated. I do not broadcast this but I feel the logo itself, along with the name is usually enough to tip people into assumption. I'm not opposed to color, but I do not want the page to scream "gay". My favourite color is yellow...

I used to be a door to door salesman so I'm doing something different where I want to do all my selling in my first meeting with the client. With this said I do not need a section for "work pictures", as I have photos of my work on my tablet, which I show the client during the consultation.

Ideally i'd like my web site to actually be just a landing page. I'd like room for all the following information within the page;

- description of services;
Weeding of Perennial and Flower Beds
Selective Pruning of Trees and Shrubs
Hedging
Landscape Construction
Landscape Design
Total Lawn Treatment Plans
Landscape Pest Control

- contact information, phone, email
Gerald Hanswick
204-731-4426
ger.hanswick@brelvanyard.com

- "free estimates" somewhere on the page that is either led to by the eye, or very easy to notice and see

- and my slogan which is "dependable, reliable, consistent"

- room for a link to my future ratewell account so they can see reviews from real people

- My Logo present

Any or all of these can be custom made graphics or simply text, whatever looks best

I do not want people to have to search for information throughout. Design it in such a way that either the eye flows naturally from one piece of information to the other, or that it's all compartmentalized neatly enough that everything is easy to find.

As I am a landscape and outdoor maintenance service I'm no opposed to images such as flowers, trees, landscaping, etc being present. However please note that my main focus and source of income comes from weeding services, everything else is bonus cash.

Many of my clients are extremely wealthy individuals who pay over $1000 for the season for me just to show up and pull weeds. So making the website appeal to wealthy people as opposed to the average joe is paramount.

I do not cut grass. Please do not have any indication on the website, either through writing or graphics that implies that I cut grass. There are enough companies doing that.

Target Market(s)

Wealthy, often elderly individuals.

Industry/Entity Type

Landscape Gardening

Coding

Coded - Design and coding required

Number of Pages Required

1 page

Font styles to use
Sans Serif

Colors

Designer to choose colors to be used in the design.

Requirements
Must have
• - description of services;
• Weeding of Perennial and Flower Beds
• Selective Pruning of Trees and Shrubs
• Hedging
• Landscape Construction
• Landscape Design
• Total Lawn Treatment Plans
• Landscape Pest Control
• - contact information, phone, email
• Gerald Hanswick
• 204-731-4426
• ger.hanswick@brelvanyard.com
• - "free estimates" somewhere on the page that is either led to by the eye, or very easy to notice and see
• - and my slogan which is "dependable, reliable, consistent"
• - room for a link to my future ratewell account so they can see reviews from real people
• - My Logo present
Nice to have
• Flowers or weeds depicted. Possibly some hardscaping and softscaping if it doesnt look too bulky and crowded.
Should not have
• grass

```html
<!DOCTYPE html>
<html lang="en">
<head>
<meta charset="utf-8">
<title>Marlow Landscaping</title>
<link href="https://fonts.googleapis.com/css2?family=Montserrat:wght@300;400;500;600;700&family=Open+Sans:wght@400;600&display=swap" rel="stylesheet">
<style>
:root{
  --yellow:#f7e400;
  --yellow-deep:#e8c800;
  --green:#0f9a4a;
  --green-soft:#e6f5ec;
  --red:#e53a3f;
  --ink:#1e1e1e;
  --grey:#555;
  --soil:#2a1d14;
  --soil-2:#3b2a1d;
  --white:#fff;
  --rainbow:#e8a23a;
}
*{box-sizing:border-box;margin:0;padding:0}
html,body{width:1200px;height:3125px;overflow:hidden}
body{position:relative;font-family:"Open Sans",Arial,sans-serif;color:var(--ink);background:var(--white)}
.section{position:absolute;left:0;width:1200px;overflow:hidden}
.abs{position:absolute}
.center{left:0;width:1200px;text-align:center}
.heading{font-family:"Montserrat",Arial,sans-serif;font-weight:300;font-size:38px;letter-spacing:.5px;color:var(--ink)}
.heading b{font-weight:700}
.divider{position:absolute;left:480px;width:240px;height:14px}
.divider::before,.divider::after{content:"";position:absolute;top:6px;width:105px;height:1px;background:#bbb}
.divider::before{left:0}.divider::after{right:0}
.divider span{position:absolute;left:114px;top:0;width:12px;height:12px;border-radius:50%;background:var(--rainbow)}
.btn{position:absolute;display:block;background:var(--yellow);border:2px solid var(--yellow-deep);border-radius:26px;font-family:"Montserrat",Arial,sans-serif;font-weight:500;font-size:17px;color:var(--ink);text-align:center;text-decoration:none}

/* hero */
.hero{top:0;height:677px}
.hero-photo{position:absolute;inset:0;background:linear-gradient(160deg,#d9dfe4 0%,#b7c79a 35%,#7a9a3a 55%,#4a3a26 78%,#2b1f16 100%)}
.hero-photo::after{content:"";position:absolute;left:0;right:0;bottom:0;height:260px;background:linear-gradient(transparent,rgba(30,20,12,.55))}
.nav{position:absolute;left:77px;top:0;width:1045px;height:83px;background:var(--white)}
.brand{font-family:"Montserrat",Arial,sans-serif;font-weight:600;color:var(--ink);letter-spacing:.5px;display:flex;align-items:center;gap:8px}
.brand i{display:inline-block;border-radius:50%;background:var(--rainbow)}
.nav .brand{position:absolute;left:30px;top:24px;font-size:30px}
.nav .brand i{width:22px;height:22px}
.menu{position:absolute;right:35px;top:31px;display:flex;gap:26px;list-style:none;font-family:"Montserrat",Arial,sans-serif;font-size:15px;color:#333}
.menu li{display:flex;align-items:center;gap:26px}
.menu li.active{font-weight:600;color:var(--ink)}
.menu .leaf{width:10px;height:18px;background:var(--green);border-radius:50% 50% 50% 50%/60% 60% 40% 40%}
.estimate{position:absolute;left:790px;top:158px;width:332px;height:362px;background:var(--yellow);border-radius:14px 0 14px 0;box-shadow:0 4px 14px rgba(0,0,0,.25)}
.estimate h2{position:absolute;top:18px;left:0;width:100%;text-align:center;font-family:"Montserrat",Arial,sans-serif;font-weight:500;color:var(--red);font-size:24px;line-height:1.1}
.estimate h2 span{display:block;font-size:37px;font-weight:600}
.field{position:absolute;left:30px;width:272px;height:40px;background:var(--white);font-size:14px;color:#777;padding:11px 12px}
.estimate .submit{position:absolute;left:30px;top:286px;width:272px;height:50px;border-radius:25px;background:var(--red);color:var(--white);font-family:"Montserrat",Arial,sans-serif;font-size:22px;font-weight:500;text-align:center;line-height:50px;box-shadow:0 3px 0 #b72529}
.slogan{top:548px;font-family:"Montserrat",Arial,sans-serif;font-size:52px;font-weight:500;color:var(--white);text-shadow:0 2px 8px rgba(0,0,0,.5)}

/* welcome */
.welcome{top:677px;height:417px;background:var(--white)}
.welcome .pre{top:52px;font-family:"Montserrat",Arial,sans-serif;font-size:22px;color:#333;letter-spacing:1px}
.welcome .title{top:86px;font-family:"Montserrat",Arial,sans-serif;font-size:40px;font-weight:300;letter-spacing:1px}
.welcome .title b{font-weight:600}
.welcome p{position:absolute;left:165px;top:186px;width:870px;text-align:center;font-size:16px;line-height:26px;color:var(--grey)}
.welcome .btn{left:507px;top:312px;width:186px;height:50px;line-height:46px}

/* services */
.services{top:1094px;height:572px}
.services-photo{position:absolute;inset:0;background:linear-gradient(90deg,#cfe0c4 0%,#eef2ea 35%,#f4f1ea 65%,#ddd7cc 100%);opacity:.9}
.services-veil{position:absolute;inset:0;background:rgba(255,255,255,.55)}
.services .heading{top:48px}
.services .divider{top:104px}
.hub{position:absolute;left:0;top:0}
.svc{position:absolute;font-family:"Montserrat",Arial,sans-serif;font-size:18px;line-height:26px;color:#2a2a2a}
.svc.r{text-align:right}

/* why */
.why{top:1666px;height:417px;background:var(--white)}
.why .heading{top:50px}
.why .divider{top:110px}
.badge{position:absolute;top:170px;width:150px;height:150px;border-radius:50%;background:var(--yellow);border:3px solid #333;display:flex;align-items:center;justify-content:center}
.badge-label{position:absolute;top:337px;width:220px;text-align:center;font-family:"Montserrat",Arial,sans-serif;font-size:18px;color:#222}
.appoint{position:absolute;left:505px;top:160px;width:190px;height:190px;border-radius:50%;background:var(--red);border:6px solid var(--white);box-shadow:0 0 0 3px var(--red);color:var(--white);font-family:"Montserrat",Arial,sans-serif;font-size:30px;line-height:40px;text-align:center;padding-top:50px}

/* weed band */
.band{top:2083px;height:259px}
.band-photo{position:absolute;inset:0;background:linear-gradient(90deg,#6f7f3a 0%,#a8a06a 30%,#9b8a6a 60%,#5d4a34 100%)}
.band-photo::after{content:"";position:absolute;inset:0;background:rgba(40,30,20,.35)}
.band h2{top:50px;font-family:"Montserrat",Arial,sans-serif;font-size:38px;font-weight:300;color:var(--white)}
.band h2 b{font-weight:600}
.band .mark{position:absolute;left:594px;top:116px;width:12px;height:12px;border-radius:50%;background:var(--white)}
.band .mark-line{position:absolute;top:122px;width:105px;height:1px;background:rgba(255,255,255,.7)}
.band .btn{left:486px;top:155px;width:228px;height:50px;line-height:46px}

/* testimonials */
.testimonials{top:2342px;height:418px;background:var(--white)}
.testimonials .heading{top:52px}
.testimonials .divider{top:108px}
.sprout{position:absolute;top:218px;width:170px;height:200px;background:linear-gradient(180deg,rgba(255,255,255,0) 0%,#cfe6a6 45%,#8fbf3c 100%);border-radius:50% 50% 0 0}
.quote{position:absolute;left:285px;top:160px;width:630px;text-align:center;font-size:14px;line-height:25px;color:var(--grey)}
.stars{top:255px;color:#f2b400;font-size:28px;letter-spacing:1px}
.client{top:300px;font-size:16px;color:var(--grey)}
.client b{color:var(--red);font-weight:400}
.soil-top{position:absolute;left:0;bottom:0;width:1200px;height:70px;background:linear-gradient(180deg,rgba(42,29,20,0),var(--soil))}

/* footer */
.footer{top:2760px;height:365px;background:linear-gradient(180deg,var(--soil) 0%,var(--soil-2) 60%,var(--soil) 100%);color:var(--white)}
.footer h3{position:absolute;top:64px;font-family:"Montserrat",Arial,sans-serif;font-size:20px;font-weight:500;letter-spacing:.5px}
.links{position:absolute;left:82px;top:115px;list-style:none;font-size:13.5px;line-height:26px}
.links li::before{content:"•";margin-right:10px}
.contact{position:absolute;left:366px;top:110px;font-size:13.5px;line-height:23px}
.contact .row{display:flex;gap:14px;margin-bottom:16px}
.contact svg{flex:none;margin-top:3px}
.footer .brand{position:absolute;left:668px;top:78px;font-size:37px;color:var(--white)}
.footer .brand i{width:26px;height:26px}
.social{position:absolute;left:810px;top:165px;display:flex;gap:18px;font-family:"Montserrat",Arial,sans-serif;font-size:14px}
.social a{display:flex;align-items:center;gap:6px;color:var(--white);text-decoration:none}
.social i{width:14px;height:14px;border-radius:50%;background:#2f5fb3}
.footer .rule{position:absolute;left:0;top:305px;width:1200px;height:1px;background:rgba(255,255,255,.15)}
.copy{top:322px;font-size:14px;color:#ddd}
.copy b{color:var(--yellow);font-weight:400}
</style>
</head>
<body>

<header class="section hero">
  <div class="hero-photo" role="img" aria-label="Gloved hands planting colourful flowers in rich garden soil"></div>
  <nav class="nav">
    <div class="brand">MARLOW LANDSCAPING <i></i></div>
    <ul class="menu">
      <li class="active">HOME</li>
      <li><span class="leaf"></span>ABOUT</li>
      <li><span class="leaf"></span>SERVICES</li>
      <li><span class="leaf"></span>CONTACT</li>
    </ul>
  </nav>
  <form class="estimate">
    <h2>GET FREE<span>ESTIMATE</span></h2>
    <div class="field" style="top:100px">Name:</div>
    <div class="field" style="top:146px">E-mail:</div>
    <div class="field" style="top:192px">Phone:</div>
    <div class="field" style="top:238px">Zipcode:</div>
    <div class="submit">Get Free Evaluation</div>
  </form>
  <div class="abs center slogan">Dependable, Reliable, Consistent</div>
</header>

<section class="section welcome">
  <div class="abs center pre">WELCOME TO</div>
  <div class="abs center title"><b>MARLOW</b> LANDSCAPING</div>
  <div class="divider" style="top:142px"><span></span></div>
  <p>Lorem Ipsum is simply dummy text of the printing and typesetting industry. Lorem Ipsum has been the industry's standard dummy text ever since the 1500s, when an unknown printer took a galley of type and scrambled it to make a type specimen book. It has survived not only five centuries, but also the leap into electronic typesetting, remaining essentially unchanged.</p>
  <a class="btn">READ MORE &raquo;</a>
</section>

<section class="section services">
  <div class="services-photo" role="img" aria-label="Soft view of a manicured garden beside a large home"></div>
  <div class="services-veil"></div>
  <h2 class="abs center heading">OUR <b>SERVICES</b></h2>
  <div class="divider"><span></span></div>
  <svg class="hub" width="1200" height="572" viewBox="0 0 1200 572">
    <circle cx="600" cy="572" r="171" fill="none" stroke="#0f9a4a" stroke-width="30"/>
    <circle cx="600" cy="572" r="155" fill="rgba(255,255,255,.35)"/>
    <circle cx="600" cy="475" r="42" fill="#e8a23a"/>
    <g stroke="#0f9a4a" stroke-width="2">
      <line x1="600" y1="231" x2="600" y2="387"/><line x1="462" y1="264" x2="524" y2="403"/>
      <line x1="737" y1="264" x2="676" y2="403"/><line x1="362" y1="356" x2="463" y2="448"/>
      <line x1="833" y1="356" x2="737" y2="448"/><line x1="327" y1="485" x2="424" y2="516"/>
      <line x1="877" y1="485" x2="776" y2="516"/>
    </g>
    <g fill="#f7e400" stroke="#0f9a4a" stroke-width="2">
      <circle cx="600" cy="387" r="6"/><circle cx="524" cy="403" r="6"/><circle cx="676" cy="403" r="6"/>
      <circle cx="463" cy="448" r="6"/><circle cx="737" cy="448" r="6"/><circle cx="424" cy="516" r="6"/><circle cx="776" cy="516" r="6"/>
    </g>
    <g fill="#fff" stroke="#0f9a4a" stroke-width="3">
      <circle cx="600" cy="231" r="52"/><circle cx="462" cy="264" r="52"/><circle cx="737" cy="264" r="52"/>
      <circle cx="362" cy="356" r="52"/><circle cx="833" cy="356" r="52"/><circle cx="327" cy="485" r="52"/><circle cx="877" cy="485" r="52"/>
    </g>
    <g fill="#0f9a4a">
      <!-- construction: tree -->
      <circle cx="600" cy="218" r="14"/><circle cx="588" cy="230" r="11"/><circle cx="612" cy="230" r="11"/><rect x="597" y="232" width="6" height="24"/>
      <!-- hedging: shears -->
      <path d="M442 244 L482 284 M482 244 L442 284" stroke="#0f9a4a" stroke-width="7" stroke-linecap="round"/>
      <!-- design: plan -->
      <rect x="717" y="244" width="40" height="40" rx="3" fill="none" stroke="#0f9a4a" stroke-width="4"/><path d="M725 276 L749 252" stroke="#0f9a4a" stroke-width="4"/>
      <!-- pruning: branch -->
      <path d="M340 378 L384 334 M356 362 L346 344 M368 350 L380 360" stroke="#0f9a4a" stroke-width="5" stroke-linecap="round"/>
      <!-- lawn plan: leaves -->
      <path d="M808 378 L815 338 L822 378 L830 332 L838 378 L846 340 L856 378 Z"/>
      <!-- weeding: hand trowel -->
      <path d="M306 506 L336 476 M336 476 L352 462 L346 484 Z" stroke="#0f9a4a" stroke-width="5" stroke-linecap="round"/><rect x="310" y="502" width="32" height="5"/>
      <!-- pest: sprayer -->
      <circle cx="877" cy="462" r="8"/><rect x="870" y="472" width="14" height="26" rx="4"/><path d="M884 478 L900 466" stroke="#0f9a4a" stroke-width="4"/><rect x="868" y="498" width="5" height="12"/><rect x="881" y="498" width="5" height="12"/>
    </g>
  </svg>
  <div class="svc" style="left:485px;top:150px;width:230px;text-align:center">Landscape Construction</div>
  <div class="svc r" style="left:230px;top:246px;width:162px">Hedging</div>
  <div class="svc" style="left:808px;top:246px">Landscape Design</div>
  <div class="svc r" style="left:60px;top:330px;width:236px">Selective Pruning of<br>Trees and Shrubs</div>
  <div class="svc" style="left:905px;top:330px">Total Lawn Treatment<br>Plans</div>
  <div class="svc r" style="left:20px;top:460px;width:236px">Weeding of Perennial<br>and Flower Beds</div>
  <div class="svc" style="left:946px;top:460px">Landscape Pest<br>Control</div>
</section>

<section class="section why">
  <h2 class="abs center heading">WHY <b>CHOOSE</b> US?</h2>
  <div class="divider"><span></span></div>
  <div class="badge" style="left:106px"><svg width="70" height="70" viewBox="0 0 24 24"><path d="M12 2l3 6.5 7 .8-5.2 4.8 1.4 7L12 17.5 5.8 21l1.4-7L2 9.3l7-.8z" fill="none" stroke="#111" stroke-width="1.8"/><path d="M8 12l3 3 8-10" fill="none" stroke="#111" stroke-width="2.4"/></svg></div>
  <div class="badge-label" style="left:71px">Excellent Service</div>
  <div class="badge" style="left:315px"><svg width="64" height="70" viewBox="0 0 24 26"><circle cx="12" cy="9" r="7" fill="#111"/><path d="M12 5l1.2 2.6 2.8.3-2.1 1.9.6 2.8L12 11.2 9.5 12.6l.6-2.8L8 7.9l2.8-.3z" fill="#f7e400"/><path d="M7 14l-3 9 4-2 2 3 2-8M17 14l3 9-4-2-2 3-2-8" fill="#111"/></svg></div>
  <div class="badge-label" style="left:280px">Guaranteed Work</div>
  <div class="appoint">APPOINT<br>US NOW</div>
  <div class="badge" style="left:733px"><svg width="78" height="66" viewBox="0 0 26 22"><path d="M13 2l10 3v6c0 5-4 8-10 10C7 19 3 16 3 11V5z" fill="#111"/><path d="M8 11l2 1.5-.6 2.3 2-1.3 2 1.3-.6-2.3L15 11" fill="none" stroke="#f7e400" stroke-width="1.2"/></svg></div>
  <div class="badge-label" style="left:698px">Quality &amp; Reliability</div>
  <div class="badge" style="left:944px"><svg width="64" height="64" viewBox="0 0 24 24"><rect x="2" y="10" width="5" height="12" fill="#111"/><path d="M8 21V10l4-7c2 0 2.5 1.5 2 3l-1 3h7c1.5 0 2 1.3 1.7 2.5l-2 7.5c-.3 1.2-1 2-2.2 2z" fill="#111"/></svg></div>
  <div class="badge-label" style="left:909px">Satisfied Customers</div>
</section>

<section class="section band">
  <div class="band-photo" role="img" aria-label="Garden path with flower beds, rubber boots and hand tools"></div>
  <h2 class="abs center">Easy <b>Solutions</b> to All Your Weed Problems</h2>
  <span class="mark-line" style="left:480px"></span><span class="mark"></span><span class="mark-line" style="left:615px"></span>
  <a class="btn">CALL US NOW &raquo;</a>
</section>

<section class="section testimonials">
  <div class="sprout" style="left:0" role="img" aria-label="Young seedlings sprouting from soil"></div>
  <div class="sprout" style="left:1030px" role="img" aria-label="Young seedlings sprouting from soil"></div>
  <div class="soil-top"></div>
  <h2 class="abs center heading">CLIENT <b>TESTIMONIALS</b></h2>
  <div class="divider"><span></span></div>
  <p class="quote">"Lorem Ipsum is simply dummy text of the printing and typesetting industry. Lorem Ipsum has been the industry's standard dummy text ever since the 1500s, when an unknown printer took a galley of type and scrambled it to make a type specimen book."</p>
  <div class="abs center stars">★★★★★</div>
  <div class="abs center client"><b>Rosa M</b>, Oak Hollow, TX</div>
</section>

<footer class="section footer">
  <h3 style="left:79px">USEFUL LINKS</h3>
  <ul class="links">
    <li>Home</li><li>About</li><li>Services</li><li>Contact</li><li>Privacy Policy</li><li>Terms &amp; Conditions</li>
  </ul>
  <h3 style="left:366px">CONTACT US</h3>
  <div class="contact">
    <div class="row"><svg width="16" height="20" viewBox="0 0 16 20"><path d="M8 0a7 7 0 0 1 7 7c0 5-7 13-7 13S1 12 1 7a7 7 0 0 1 7-7z" fill="#fff"/><circle cx="8" cy="7" r="2.6" fill="#2a1d14"/></svg><div>Gerald Hanswick<br>123 Building Name,Area, City<br>State - Country</div></div>
    <div class="row"><svg width="16" height="16" viewBox="0 0 24 24"><path d="M6.6 10.8a15 15 0 0 0 6.6 6.6l2.2-2.2c.3-.3.7-.4 1-.2 1.1.4 2.3.6 3.6.6.6 0 1 .4 1 1V20c0 .6-.4 1-1 1A17 17 0 0 1 3 4c0-.6.4-1 1-1h3.5c.6 0 1 .4 1 1 0 1.3.2 2.5.6 3.6.1.3 0 .7-.2 1z" fill="#fff"/></svg><div>204-731-4426</div></div>
    <div class="row"><svg width="18" height="14" viewBox="0 0 18 14"><rect width="18" height="14" rx="1" fill="#fff"/><path d="M1 1l8 6 8-6" fill="none" stroke="#2a1d14" stroke-width="1.5"/></svg><div>ger.hanswick@brelvanyard.com</div></div>
  </div>
  <div class="brand">MARLOW LANDSCAPING <i></i></div>
  <div class="social">
    <a><i></i>Chatterly</a><a><i></i>Snapgram</a><a><i></i>ratewell</a>
  </div>
  <div class="rule"></div>
  <div class="abs center copy">© <b>MARLOW LANDSCAPING</b> – 2017. All Rights Reserved.</div>
</footer>

</body>
</html>
```